Building Company Business Card Design

Need a design for a business card:
It needs to have: Name, Phone, Facebook link, Website, email
i would also like a list of works we undertake:
-New Homes
-Extensions, Renovations & Bathrooms
-Decking, Carports, Sheds (Residential and Industrial)
-Carpentry
-Fences, Patios & Pergolas

Name, Phone, Facebook link, Website, email + details of services provided listed in description

```html
<!DOCTYPE html>
<html lang="en">
<head>
<meta charset="utf-8">
<title>Bayline Homes – Business Card</title>
<link href="https://fonts.googleapis.com/css2?family=Roboto:wght@300;400;500;700&display=swap" rel="stylesheet">
<style>
  :root {
    --bg: #d3d8d8;
    --card: #ffffff;
    --green: #3bb54a;
    --ink: #1b1b1b;
    --grey: #7d7d7d;
  }
  * { box-sizing: border-box; margin: 0; padding: 0; }
  html, body { width: 1200px; height: 960px; overflow: hidden; }
  body {
    background: var(--bg);
    font-family: 'Roboto', Arial, sans-serif;
    color: var(--ink);
    position: relative;
  }
  .card {
    position: absolute;
    top: 130px;
    width: 401px;
    height: 701px;
    background: var(--card);
    border-radius: 24px;
    overflow: hidden;
  }
  .card--front { left: 171px; }
  .card--back { left: 627px; }

  /* Front */
  .front-mark {
    position: absolute;
    left: 140px;
    top: 325px;
    width: 44px;
    height: 44px;
    background: var(--green);
  }
  .front-name {
    position: absolute;
    left: 270px;
    top: 352px;
    width: 490px;
    transform: translate(-50%, -50%) rotate(-90deg);
    text-align: center;
    color: var(--ink);
    font-weight: 700;
    line-height: 1;
  }
  .front-name__main { display: block; font-size: 56px; letter-spacing: 1px; }
  .front-name__sub { display: block; font-size: 29px; letter-spacing: 2px; margin-top: 6px; }

  /* Back */
  .brand {
    position: absolute;
    top: 40px;
    left: 0;
    width: 100%;
    text-align: center;
    color: var(--ink);
    font-weight: 700;
    line-height: 1;
  }
  .brand__mark {
    display: block;
    width: 34px;
    height: 34px;
    margin: 0 auto 18px;
    background: var(--green);
  }
  .brand__main { display: block; font-size: 31px; letter-spacing: 0.5px; }
  .brand__sub { display: block; font-size: 14.5px; letter-spacing: 1.2px; margin-top: 3px; }

  .person {
    position: absolute;
    top: 332px;
    width: 100%;
    text-align: center;
  }
  .person__name { font-size: 35px; color: var(--green); line-height: 1; }
  .person__first { font-weight: 700; }
  .person__last { font-weight: 300; }
  .person__role { font-size: 17px; font-weight: 400; margin-top: 4px; color: var(--ink); }

  .icon-row {
    position: absolute;
    top: 400px;
    left: 77px;
    width: 244px;
    height: 24px;
    display: flex;
    align-items: center;
    justify-content: center;
    gap: 10px;
  }
  .icon-row__rule { flex: 1; height: 2px; background: var(--green); }
  .icon-row svg { width: 24px; height: 24px; }

  .contacts {
    position: absolute;
    top: 428px;
    width: 100%;
    list-style: none;
    text-align: center;
    font-size: 15.5px;
    line-height: 22.3px;
    letter-spacing: 0.3px;
  }

  .services {
    position: absolute;
    left: 0;
    bottom: 0;
    width: 100%;
    height: 151px;
    background: var(--green);
    border-top: 3px solid var(--ink);
  }
  .services__tag {
    position: absolute;
    top: -17px;
    left: 50%;
    transform: translateX(-50%);
    width: 128px;
    height: 30px;
    border-radius: 50%;
    background: var(--green);
    border: 2px solid var(--card);
    box-shadow: 0 0 0 1.5px var(--ink);
    color: var(--card);
    font-weight: 500;
    font-size: 18px;
    text-align: center;
    line-height: 26px;
  }
  .services__list {
    margin-top: 24px;
    text-align: center;
    color: var(--card);
    font-size: 15.5px;
    line-height: 22.3px;
    letter-spacing: 0.2px;
  }
  .services__list p { white-space: nowrap; }
</style>
</head>
<body>

<section class="card card--front" aria-label="Card front">
  <span class="front-mark" aria-hidden="true"></span>
  <h1 class="front-name">
    <span class="front-name__main">BAYLINE HOMES</span>
    <span class="front-name__sub">AND BUILDS PTY LTD</span>
  </h1>
</section>

<section class="card card--back" aria-label="Card back">
  <div class="brand">
    <span class="brand__mark" aria-hidden="true"></span>
    <span class="brand__main">BAYLINE HOMES</span>
    <span class="brand__sub">AND BUILDS PTY LTD</span>
  </div>

  <div class="person">
    <p class="person__name"><span class="person__first">Mara</span> <span class="person__last">Velinska</span></p>
    <p class="person__role">Founder &amp; CEO</p>
  </div>

  <div class="icon-row" aria-hidden="true">
    <span class="icon-row__rule"></span>
    <svg viewBox="0 0 24 24"><rect x="4" y="4" width="16" height="16" rx="3" transform="rotate(45 12 12)" fill="#3bb54a"/><path d="M9 8.2l1.4-.4 1 2-1 .8a5 5 0 0 0 2.6 2.6l.8-1 2 1-.4 1.4c-3.3.4-6.8-3.1-6.4-6.4z" fill="#fff"/></svg>
    <svg viewBox="0 0 24 24"><rect x="4" y="4" width="16" height="16" rx="3" transform="rotate(45 12 12)" fill="#3bb54a"/><circle cx="12" cy="12" r="4" fill="none" stroke="#fff" stroke-width="1.4"/></svg>
    <svg viewBox="0 0 24 24"><rect x="4" y="4" width="16" height="16" rx="3" transform="rotate(45 12 12)" fill="#3bb54a"/><circle cx="12" cy="12" r="4.2" fill="none" stroke="#fff" stroke-width="1.2"/><path d="M7.8 12h8.4M12 7.8c-2 2.4-2 6 0 8.4M12 7.8c2 2.4 2 6 0 8.4" fill="none" stroke="#fff" stroke-width="1"/></svg>
    <svg viewBox="0 0 24 24"><rect x="4" y="4" width="16" height="16" rx="3" transform="rotate(45 12 12)" fill="#3bb54a"/><rect x="8" y="9.2" width="8" height="5.8" fill="none" stroke="#fff" stroke-width="1.2"/><path d="M8 9.4l4 3 4-3" fill="none" stroke="#fff" stroke-width="1.2"/></svg>
    <span class="icon-row__rule"></span>
  </div>

  <ul class="contacts">
    <li>(555) 014-2290</li>
    <li>@baylinehomes</li>
    <li>www.baylinehomes.com</li>
    <li>info@baylinehomes.com</li>
  </ul>

  <div class="services">
    <span class="services__tag">SERVICES</span>
    <div class="services__list">
      <p>● New Homes ● Extensions</p>
      <p>● Renovations &amp; Bathrooms ● Decking ● Carports</p>
      <p>● Sheds (Residential and Industrial) ● Carpentry</p>
      <p>● Fences ● Patios &amp; Pergolas</p>
    </div>
  </div>
</section>

</body>
</html>
```